Original catchy book cover

I need a book cover for my book "The Steady Harbor Manual" (https://quillpress.example/harbormanual). This will be a book self published on brightmart.
The book talks about the following concepts:
- Iterative product delivery
- Early discovery using feedback from customers
- Start small, think big, move fast
- Slice the product into valuable increments that can be validated with customers
- Experimental approach to deciding the next slice of work
A simple cover that stands out from the business books already out there! Some examples are:
https://www.brightmart.example/Field-Notes-Thriving-Teams-Steadily-ebook/dp/Q00XTR4KWZ/ref=sr_1_1?ie=UTF8&qid=1500000001&sr=8-1&keywords=field+notes
https://www.brightmart.example/Quiet-Harbor-Almanac-Shape-Offerings-ebook/dp/Q00MVK219J/ref=sr_1_1?s=digital-text&ie=UTF8&qid=1500000002&sr=1-1&keywords=quiet+harbor+almanac
https://www.brightmart.example/Course-Charts-Renewed-Heading-Fog-ebook/dp/Q099WT71ZD/ref=pd_sim_351_2?_encoding=UTF8&psc=1&refRID=9QZTRWJDDAV52LM0NKPP
Lastly, attached are 2 draft covers that i've been playing with. Would love a graphic as part of the cover if it makes sense in your design! The graphic should tie to the meaning or themes of the book. Emphasis on ways of working, collaboration, experimentation, hypothesis, agile, incremental or adaptive. Those are some words that describe the content of the book.
Alternatively, something abstract could also be an option if a literal graphic doesn't suit the theme of your design.
Target Market(s)
Product owners, scrum masters, people in the agile community, software developers, designers
Industry/Entity Type
Information Technology
Font styles to use
Colors
Designer to choose colors to be used in the design.
Requirements
Must have
- Title, Subtitle, Author Name
- Back of the book should have space for a description (use lorem ipsum for now)
- Please use the editorial logo
- (please omit "created by Tomas Verlindt" because the editorial logo replaces that.
- The design must be original art or graphics (i.e. it should be similar to another cover in this topic).
Nice to have
- A graphic would be ideal if it is relevant to the book topic, otherwise a nice simple cover that uses colors or patterns that are easy to recall.
- The color suggestions below are suggestions only. Do not feel you have to incorporate all the colors and feel free to recommend an alternate palette.
Should not have
- Clipart or generic stock art photos. Images for the sake of images, traditional logos (e.g. a computer, a phone etc unless it's part of an overall theme that ties the logos together).

```html
<!DOCTYPE html>
<html lang="en">
<head>
<meta charset="utf-8">
<title>The Steady Harbor Manual — Book Cover Spread</title>
<link rel="stylesheet" href="https://fonts.googleapis.com/css2?family=Bebas+Neue&family=EB+Garamond:wght@400&family=Oswald:wght@300;500&display=swap">
<style>
  :root {
    --magenta: #d0177c;
    --spine-pink: #e9218d;
    --ink: #111111;
    --paper: #ffffff;
    --bulb-pink: #f4c6e1;
    --bulb-pink-deep: #e79bc8;
    --amber: #f0b25a;
  }
  * { margin: 0; padding: 0; box-sizing: border-box; }
  html, body { width: 1200px; height: 830px; overflow: hidden; background: var(--paper); }
  .spread { position: relative; width: 1200px; height: 830px; background: var(--paper); overflow: hidden; }

  /* Back cover */
  .back-cover { position: absolute; left: 0; top: 0; width: 554px; height: 830px; }
  .back-description {
    position: absolute; left: 62px; top: 60px; width: 435px;
    font-family: "EB Garamond", Georgia, serif;
    font-size: 17.4px; line-height: 20px; color: var(--ink);
    text-align: justify; hyphens: auto;
  }
  .back-description p + p { margin-top: 20px; }
  .back-bulb-art {
    position: absolute; left: 0; top: 436px; width: 226px; height: 394px;
    background: radial-gradient(ellipse 120% 90% at 10% 55%, var(--bulb-pink-deep) 0%, var(--bulb-pink) 55%, rgba(255,255,255,0) 100%);
    border-top-right-radius: 60% 45%;
  }
  .barcode-space {
    position: absolute; left: 62px; top: 702px; width: 130px; height: 80px;
    background: var(--paper);
  }

  /* Spine */
  .spine {
    position: absolute; left: 554px; top: 0; width: 92px; height: 830px;
    background: var(--spine-pink); color: var(--paper);
  }
  .spine-title {
    position: absolute; left: 50%; top: 54px; transform: translateX(-50%);
    writing-mode: vertical-rl;
    font-family: "Bebas Neue", "Oswald", sans-serif;
    font-size: 42px; letter-spacing: 1px; white-space: nowrap;
  }
  .spine-author {
    position: absolute; left: 50%; top: 592px; transform: translateX(-50%);
    writing-mode: vertical-rl;
    font-family: "Oswald", sans-serif; font-weight: 300;
    font-size: 22px; letter-spacing: 5px; white-space: nowrap;
  }

  /* Front cover */
  .front-cover { position: absolute; left: 646px; top: 0; width: 554px; height: 830px; text-align: center; }
  .front-title {
    position: absolute; left: 0; right: 0; top: 40px;
    font-family: "Bebas Neue", "Oswald", sans-serif; font-weight: 400;
    color: var(--magenta); line-height: 0.9;
  }
  .front-title .line-1 { display: block; font-size: 134px; }
  .front-title .line-2 { display: block; font-size: 94px; margin-top: 12px; }
  .front-subtitle {
    position: absolute; left: 0; right: 0; top: 294px;
    font-family: "Oswald", sans-serif; font-weight: 500;
    font-size: 26px; line-height: 38px; letter-spacing: 2.5px; color: var(--ink);
    white-space: nowrap;
  }
  .front-bulb-art {
    position: absolute; left: 30px; top: 384px; width: 496px; height: 348px;
    background:
      radial-gradient(ellipse 22% 38% at 50% 42%, var(--amber) 0%, rgba(240,178,90,0.6) 60%, rgba(240,178,90,0) 100%),
      radial-gradient(ellipse 50% 30% at 50% 50%, rgba(208,23,124,0.75) 0%, rgba(208,23,124,0.35) 70%, rgba(255,255,255,0) 100%);
  }
  .front-author {
    position: absolute; left: 0; right: 0; top: 752px;
    font-family: "Oswald", sans-serif; font-weight: 500;
    font-size: 44px; line-height: 1; letter-spacing: 22px; padding-left: 22px;
    color: var(--spine-pink);
  }
</style>
</head>
<body>
<main class="spread">
  <section class="back-cover">
    <div class="back-description">
      <p>Lorem ipsum dolor sit amet, consectetur adipiscing elit. Duis non cursus lorem. Nunc id ante elit. In malesuada orci aliquam tincidunt bibendum. Quisque neque eros, fermentum ac pretium id, interdum luctus dui. Ut nisi urna, rutrum eu nisi ultrices, tristique dapibus enim. Nunc tempus mi efficitur nulla placerat, id bibendum lacus feugiat. Maecenas faucibus suscipit luctus. Mauris sit amet justo congue elit pellentesque pharetra lacinia eget felis. Vivamus sed mollis sapien.</p>
      <p>Integer euismod ex justo, sollicitudin porttitor odio posuere ac. Aliquam hendrerit accumsan quam, nec interdum ante fringilla in. Aliquam lobortis metus sit amet ornare tempus. Sed tincidunt tellus quis tempor consequat. Aenean eget magna neque. Nam id sollicitudin orci. Donec ut leo ac nibh consectetur vehicula a quis nunc. Donec nec neque quis erat finibus scelerisque. Nullam egestas tempor libero eu consectetur. Ut quis turpis nec mi maximus ultrices at at eros. Maecenas sit amet efficitur tortor.</p>
    </div>
    <div class="back-bulb-art" role="img" aria-label="Faint pink light bulb photo with hand-drawn planning sketches inside"></div>
    <div class="barcode-space"></div>
  </section>

  <section class="spine">
    <div class="spine-title">THE STEADY HARBOR MANUAL</div>
    <div class="spine-author">MARA QUELL</div>
  </section>

  <section class="front-cover">
    <h1 class="front-title">
      <span class="line-1">THE STEADY</span>
      <span class="line-2">HARBOR MANUAL</span>
    </h1>
    <p class="front-subtitle">A FIELD HANDBOOK FOR SHAPING STEADY<br>OFFERINGS THAT TEAMS CAN TRUST</p>
    <div class="front-bulb-art" role="img" aria-label="Glowing light bulb filled with planning sketches, circled by two magenta cycle arrows"></div>
    <p class="front-author">MARA QUELL</p>
  </section>
</main>
</body>
</html>
```